Ferncrest Dental, LLC business card project

Business card to be designed with current logo.
Dental office- please keep design of card that looks clean and professional.
Please include the following info:
Ferncrest Dental, LLC
Dr. Lorna Pettigrew
2871 Marlowe Street
Bethlehem, PA 18093
610-555-0193
ferncrestdental.office@examplemail.test
Hello everyone-
Reason: Just got back from overseas- will look at all designs and provide feedback. Thank you!
Reason: Polling my friends for the final selection-
thank you to all those that participated- so many talented designers!

```html
<!DOCTYPE html>
<html lang="en">
<head>
<meta charset="utf-8">
<title>Ferncrest Dental, LLC – Business Card</title>
<link rel="stylesheet" href="https://fonts.googleapis.com/css2?family=Comfortaa:wght@400&family=Tinos:wght@400;700&display=swap">
<style>
  :root {
    --page-bg: #f6f6f6;
    --card-border: #dddddd;
    --card-face: #ffffff;
    --card-back: #cfcfcf;
    --brand-green: #8cc63f;
    --ink: #222222;
    --ink-soft: #555555;
    --label-bg: #d9d9d9;
    --mark-grey: #b5b5b5;
  }
  * { margin: 0; padding: 0; box-sizing: border-box; }
  html, body { width: 1200px; height: 1000px; overflow: hidden; }
  body { background: var(--page-bg); position: relative; font-family: "Tinos", "Times New Roman", serif; }

  .card { position: absolute; top: 190px; width: 370px; height: 455px; }
  .card--front { left: 150px; }
  .card--back { left: 690px; }
  .card svg { position: absolute; inset: 0; overflow: visible; }

  .tooth-outline { fill: var(--card-face); stroke: var(--card-border); stroke-width: 22; stroke-linejoin: round; filter: drop-shadow(0 6px 10px rgba(0,0,0,0.12)); }
  .tooth-back { fill: var(--card-back); filter: drop-shadow(0 6px 10px rgba(0,0,0,0.12)); }
  .info-panel { fill: var(--card-face); }
  .brand-dot { fill: var(--mark-grey); }

  .brand-name {
    position: absolute; left: 0; right: 0; top: 150px;
    text-align: center;
    font-family: "Comfortaa", "Trebuchet MS", sans-serif;
    font-weight: 400; font-size: 25px; letter-spacing: -0.5px;
    color: var(--brand-green);
    white-space: nowrap;
  }

  .contact { position: absolute; left: 60px; top: 64px; color: var(--ink-soft); font-size: 19px; line-height: 1.15; }
  .contact__name { color: var(--ink); font-weight: 700; font-size: 22px; margin-bottom: 14px; white-space: nowrap; }
  .contact__phone { margin-bottom: 12px; }
  .contact__address { margin-bottom: 12px; }
  .contact__email { font-size: 14.5px; white-space: nowrap; }

  .side-label {
    position: absolute; top: 688px; height: 32px; padding: 0 6px;
    line-height: 32px; font-size: 19px; color: #444;
    background: linear-gradient(#ececec, var(--label-bg));
  }
  .side-label--front { left: 300px; }
  .side-label--back { left: 831px; }
</style>
</head>
<body>

  <section class="card card--front" aria-label="Card front">
    <svg viewBox="0 0 370 455" width="370" height="455">
      <path class="tooth-outline" d="M40,60 C20,100 15,170 40,230 C60,280 70,330 75,380 C80,430 95,455 120,450 C140,445 140,400 142,360 C145,300 155,250 185,250 C215,250 225,300 228,360 C230,400 230,445 250,450 C275,455 290,430 295,380 C300,330 310,280 330,230 C355,170 350,100 330,60 C310,20 270,5 230,15 C210,20 200,25 185,25 C170,25 160,20 140,15 C100,5 60,20 40,60 Z"/>
    </svg>
    <p class="brand-name">Ferncrest Dental, LLC</p>
  </section>

  <section class="card card--back" aria-label="Card back">
    <svg viewBox="0 0 370 455" width="370" height="455">
      <defs>
        <clipPath id="tooth-inner">
          <path d="M52,66 C34,104 30,170 52,226 C60,246 64,252 66,258 L304,258 C306,252 310,246 318,226 C340,170 336,104 318,66 C300,32 266,20 232,28 C212,32 200,37 185,37 C170,37 158,32 138,28 C104,20 70,32 52,66 Z"/>
        </clipPath>
      </defs>
      <path class="tooth-back" d="M40,60 C20,100 15,170 40,230 C60,280 70,330 75,380 C80,430 95,455 120,450 C140,445 140,400 142,360 C145,300 155,250 185,250 C215,250 225,300 228,360 C230,400 230,445 250,450 C275,455 290,430 295,380 C300,330 310,280 330,230 C355,170 350,100 330,60 C310,20 270,5 230,15 C210,20 200,25 185,25 C170,25 160,20 140,15 C100,5 60,20 40,60 Z"/>
      <path class="info-panel" clip-path="url(#tooth-inner)" d="M20,20 L350,20 L350,232 C325,236 300,236 272,242 C242,248 215,254 185,254 C155,254 128,248 98,242 C70,236 45,236 20,232 Z"/>
      <circle class="brand-dot" cx="298" cy="76" r="10"/>
    </svg>
    <div class="contact">
      <p class="contact__name">Dr. Lorna Pettigrew</p>
      <p class="contact__phone">610-555-0193</p>
      <p class="contact__address">2871 Marlowe Street<br>Bethlehem, PA 18093</p>
      <p class="contact__email">ferncrestdental.office@examplemail.test</p>
    </div>
  </section>

  <span class="side-label side-label--front">FRONT</span>
  <span class="side-label side-label--back">BACK</span>

</body>
</html>
```